Business Card Design for ClearPathVitality

We need the new logo on a business card for 3 employees:
Nora Kettering, PhD, Advanced Instructor and Practitioner of SomaLink Integral Medicine (email: nora@clearpathvitality.com)
Ray Holm, Business Manager (email: ray@clearpathvitality.com)
Bea Marlowe, Administrative Assistant (email: bea@helixsense.com)

Target Market(s)

healthcare professionals

Industry/Entity Type

Alternative Medicine

Contact Information for Business Card

Names, titles, emails (names, titles, emails are in project description), phone, address, website, with logo and tagline. See below for address, phone, website: 418 Alder Ln, Bldg 12, Ste 305
Harlow Bay, OR 97499
541-555-2746
www.clearpathvitality.com
Tagline: Roots of Balance, Light of Renewal

Font styles to use
Other font styles liked:
• Gabriela

Colors
00a990
86cfc6
6b449b
b7a5cd
85abd2
abd036

Requirements
Must have
• Colors and style that match the logo design - shades such as blue, green, purple
• Compatible or same font as in the logo
Nice to have
• Nice if it goes with the theme of Nora's last business card - uploaded below
Should not have
• colors or style in conflict with the logo

```html
<!DOCTYPE html>
<html lang="en">
<head>
<meta charset="utf-8">
<title>ClearPathVitality Business Card</title>
<link rel="stylesheet" href="https://fonts.googleapis.com/css2?family=Gabriela&family=Lato:wght@400;700&family=Raleway:wght@400&display=swap">
<style>
  :root {
    --backdrop: #e9edf1;
    --card: #ffffff;
    --purple: #6b449b;
    --navy: #2e2a6b;
    --title-blue: #5a74b6;
    --ink: #333333;
    --rule: #2b2b2b;
    --teal: #1c96a4;
    --blue: #2a4c98;
    --green: #7fbf3a;
    --white: #ffffff;
  }
  * { box-sizing: border-box; margin: 0; padding: 0; }
  html, body { width: 1200px; height: 1000px; overflow: hidden; }
  body { background: var(--backdrop); position: relative; font-family: "Lato", sans-serif; }

  .card { position: absolute; left: 261px; width: 675px; height: 385px; background: var(--card); box-shadow: 0 6px 18px rgba(0,0,0,0.18); }
  .card-front { top: 82px; }
  .card-back { top: 527px; overflow: hidden; }

  .brand { position: absolute; left: 150px; top: 140px; display: flex; align-items: center; gap: 18px; }
  .brand-dot { width: 78px; height: 78px; border-radius: 50%; background: var(--green); }
  .brand-name { font-family: "Gabriela", serif; font-size: 38px; color: var(--purple); }
  .tagline { position: absolute; left: 0; right: 0; top: 292px; text-align: center; font-family: "Raleway", sans-serif; font-size: 25px; color: var(--navy); }

  .staff { position: absolute; left: 0; top: 0; width: 338px; height: 385px; }
  .person { position: absolute; left: 23px; width: 300px; }
  .person-name { font-family: "Gabriela", serif; font-size: 26px; color: var(--purple); line-height: 1; margin-left: 13px; }
  .person-title { font-size: 15px; color: var(--title-blue); line-height: 19px; margin-left: 38px; margin-top: 5px; }
  .person-email { display: flex; align-items: center; gap: 8px; margin-left: 38px; margin-top: 8px; font-size: 17.5px; color: var(--ink); }
  .person-email svg { width: 18px; height: 13px; }
  .divider { position: absolute; left: 23px; width: 300px; height: 2px; background: var(--rule); }

  .contact-panel { position: absolute; left: 338px; top: 0; width: 337px; height: 385px; }
  .contact-backdrop { position: absolute; inset: 0; background: linear-gradient(160deg, var(--teal) 0%, #1f7fa6 45%, var(--blue) 100%); }
  .contact-info { position: absolute; inset: 0; color: var(--white); }
  .phone { position: absolute; left: 37px; top: 170px; display: flex; align-items: center; gap: 14px; font-size: 29px; }
  .phone svg { width: 26px; height: 26px; }
  .address { position: absolute; left: 37px; top: 253px; font-size: 18px; line-height: 23px; }
  .website { position: absolute; left: 37px; top: 334px; font-size: 18.5px; font-weight: 700; }
</style>
</head>
<body>
  <section class="card card-front">
    <div class="brand">
      <span class="brand-dot"></span>
      <span class="brand-name">ClearPathVitality</span>
    </div>
    <p class="tagline">Light of Renewal</p>
  </section>

  <section class="card card-back">
    <div class="staff">
      <div class="person" style="top:35px;">
        <p class="person-name">Nora Kettering</p>
        <p class="person-title">PhD, Advanced Instructor and<br>Practitioner of SomaLink<br>Integral Medicine</p>
        <p class="person-email"><svg viewBox="0 0 18 13"><rect width="18" height="13" fill="#222"/><path d="M1 1 L9 7 L17 1" stroke="#fff" stroke-width="1.4" fill="none"/></svg>nora@clearpathvitality.com</p>
      </div>
      <div class="divider" style="top:166px;"></div>
      <div class="person" style="top:184px;">
        <p class="person-name">Ray Holm</p>
        <p class="person-title">Business Manager</p>
        <p class="person-email"><svg viewBox="0 0 18 13"><rect width="18" height="13" fill="#222"/><path d="M1 1 L9 7 L17 1" stroke="#fff" stroke-width="1.4" fill="none"/></svg>ray@clearpathvitality.com</p>
      </div>
      <div class="divider" style="top:271px;"></div>
      <div class="person" style="top:284px;">
        <p class="person-name">Bea Marlowe</p>
        <p class="person-title">Administrative Assistant</p>
        <p class="person-email" style="margin-top:0;"><svg viewBox="0 0 18 13"><rect width="18" height="13" fill="#222"/><path d="M1 1 L9 7 L17 1" stroke="#fff" stroke-width="1.4" fill="none"/></svg>bea@helixsense.com</p>
      </div>
    </div>

    <div class="contact-panel">
      <div class="contact-backdrop" role="img" aria-label="Soft teal-to-blue image of a glowing DNA double helix"></div>
      <div class="contact-info">
        <p class="phone"><svg viewBox="0 0 24 24"><path fill="#fff" d="M6.6 10.8a15.1 15.1 0 0 0 6.6 6.6l2.2-2.2a1 1 0 0 1 1-.25 11.4 11.4 0 0 0 3.6.57 1 1 0 0 1 1 1V20a1 1 0 0 1-1 1A17 17 0 0 1 3 4a1 1 0 0 1 1-1h3.5a1 1 0 0 1 1 1c0 1.25.2 2.45.57 3.57a1 1 0 0 1-.25 1z"/></svg>541-555-2746</p>
        <p class="address">418 Alder Ln, Bldg 12, Ste 305<br>Harlow Bay, OR 97499</p>
        <p class="website">www.clearpathvitality.com</p>
      </div>
    </div>
  </section>
</body>
</html>
```